Brindle Structures Construction Company Seeking Modern Website

We are a small construction company wanting to create a web presence. We don't have much in the way of current content but will get photos as they come in. Attached is a picture of our business card.
The pages we would like on the menu are:
Home
Portfolio
Product Specs
Testimonials
Our Process
Contact
Some designs we like are:
http://www.tovenquarnsheds.example/
http://www.qzrsheds.example/
http://pannowsheds.example/
http://wistenhalls.example/
Not much requirements other than that so feel free to be creative!
Updates
Target Market(s)
Construction
Commercial and Residential Buildings
Industry/Entity Type
Construction Company
Number of Pages Required
5+ page
Look and feel

```html
<!DOCTYPE html>
<html lang="en">
<head>
<meta charset="utf-8">
<title>Brindle Structures</title>
<link rel="stylesheet" href="https://fonts.googleapis.com/css2?family=Open+Sans:wght@300;400;600;700&family=Dancing+Script:wght@600&display=swap">
<style>
:root{
  --accent:#e2533c;
  --blue:#1aa3d9;
  --sky:#00a0e0;
  --ink:#444;
  --muted:#666;
  --paper:#ffffff;
  --soft:#f3f3f3;
  --grey:#ececea;
  --footer:#2c2c2c;
  --footer-deep:#1c1c1c;
  --footer-line:#4a4a4a;
}
*{box-sizing:border-box;margin:0;padding:0}
html,body{width:1200px;height:3543px;overflow:hidden}
body{font-family:"Open Sans",Arial,sans-serif;color:var(--ink);background:var(--paper);position:relative}
.abs{position:absolute}
.section-title{position:absolute;left:0;width:1200px;text-align:center;font-weight:300;font-size:30px;color:var(--accent);letter-spacing:1px;text-transform:uppercase}
.lead{position:absolute;left:80px;width:1040px;text-align:center;font-size:14px;line-height:24px;color:var(--ink)}

/* header */
.site-header{position:absolute;top:0;left:0;width:1200px;height:85px;background:#fbfcfd}
.brand{position:absolute;left:80px;top:22px;display:flex;align-items:center;gap:10px;font-weight:700;font-size:28px;color:#1d63c4}
.brand-dot{width:16px;height:16px;border-radius:50%;background:var(--accent)}
.main-nav{position:absolute;right:78px;top:38px;display:flex;gap:20px;font-size:16px;text-transform:uppercase}
.main-nav a{color:var(--blue);text-decoration:none}
.main-nav a.active{color:var(--accent)}

/* hero */
.hero{position:absolute;top:85px;left:0;width:1200px;height:489px;background:linear-gradient(180deg,#6aa3dc 0%,#b9d4ee 28%,#7a726c 45%,#5f5750 70%,#3f6a2c 92%,#4a7a32 100%)}
.hero-title{position:absolute;top:200px;left:0;width:1200px;text-align:center;font-family:"Dancing Script",cursive;font-size:50px;color:#bff0fb;letter-spacing:1px}

/* services */
.services{position:absolute;top:574px;left:0;width:1200px;height:560px;background:var(--soft)}
.service{position:absolute;top:184px;width:241px}
.service-photo{width:241px;height:189px;border:2px solid #4bb6e0}
.service h3{margin-top:44px;font-weight:400;font-size:15.5px;color:var(--blue);text-transform:uppercase;letter-spacing:.5px}
.service p{margin-top:18px;font-size:13.5px;line-height:19px;color:var(--muted)}

/* process */
.process{position:absolute;top:1134px;left:0;width:1200px;height:387px;background:var(--paper)}
.step{position:absolute;top:118px;width:320px;text-align:center}
.step-icon{width:86px;height:86px;border-radius:50%;margin:0 auto;display:flex;align-items:center;justify-content:center}
.step h3{margin-top:30px;font-weight:400;font-size:21px;color:var(--blue);text-transform:uppercase}
.step p{margin:14px auto 0;width:250px;font-size:13px;line-height:21px;color:var(--muted)}

/* portfolio */
.portfolio{position:absolute;top:1521px;left:0;width:1200px;height:824px;background:var(--grey)}
.tile{position:absolute}

/* products */
.products{position:absolute;top:2345px;left:0;width:1200px;height:494px;background:var(--sky)}
.products .section-title{color:#10324a}
.products .lead{color:#fff;font-weight:600;font-size:13.5px}
.carousel{position:absolute;top:187px;left:123px;width:959px;height:241px;background:#fff}
.product-feature{position:absolute;left:4px;top:4px;width:312px;height:233px;background:linear-gradient(160deg,#3f6fb3,#2c5599);border:3px solid #fff;outline:2px solid #2c5599;color:#fff;text-align:center}
.product-feature h4{margin-top:50px;font-weight:400;font-size:20px}
.product-feature p{font-size:14px;line-height:18px}
.btn{display:inline-block;margin-top:22px;background:#fff;color:#2c5599;font-size:14px;padding:6px 12px}
.arrow{position:absolute;width:58px;height:58px;border-radius:50%;background:#15608f;border:3px solid #fff}

/* testimonials */
.testimonials{position:absolute;top:2839px;left:0;width:1200px;height:354px;background:var(--paper)}
.quote-card{position:absolute;top:104px;width:489px;height:142px;border:2px solid #2f2f2f;border-radius:6px;background:#fff}
.quote-card .mark{position:absolute;font-size:110px;line-height:1;color:#e6eef3;font-family:Georgia,serif}
.quote-card p{position:relative;margin:22px 24px 0;font-size:12px;line-height:18px;color:#333}
.quote-card .who{position:relative;margin:10px 24px 0;font-size:12px;font-weight:700;color:#222}
.quote-card .role{margin:0 24px;font-size:11px;color:#444;position:relative}
.avatar{position:absolute;width:96px;height:96px;border-radius:50%;border:4px solid #2aa6d7;background:#fff;padding:4px}
.avatar span{display:block;width:100%;height:100%;border-radius:50%;background:linear-gradient(180deg,#8a9aa8,#3b4654)}

/* footer */
.site-footer{position:absolute;top:3193px;left:0;width:1200px;height:303px;background:var(--footer);color:#ddd}
.foot-col{position:absolute;top:30px}
.foot-col h5{font-weight:400;font-size:15px;color:var(--blue);padding-bottom:8px;border-bottom:1px solid var(--footer-line);margin-bottom:8px}
.foot-nav li{list-style:none;font-size:12px;line-height:15px;padding:8px 8px;border-bottom:1px solid var(--footer-line)}
.news-thumb{float:left;width:120px;height:110px;margin:8px 10px 4px 0;border:2px solid #666;background:linear-gradient(180deg,#6a7e93,#3a3b3c)}
.news p{font-size:12.5px;line-height:15px}
.loc-line{display:flex;gap:10px;align-items:flex-start;font-size:11.5px;line-height:15px;margin-top:8px}
.map{width:238px;height:106px;margin-top:14px;border:3px solid #999;background:linear-gradient(135deg,#dfe4d8,#c9d4e2)}
.signup p{font-size:11.5px;line-height:16px}
.signup-form{display:flex;align-items:center;margin-top:8px;background:#fff;width:242px;height:26px;padding:2px}
.signup-form span{flex:1;font-size:11px;color:#666;padding-left:8px}
.signup-form b{background:var(--blue);color:#fff;font-weight:400;font-size:11px;padding:3px 6px}
.social{display:flex;gap:8px;margin-top:22px;margin-left:92px}
.social i{display:block;width:28px;height:28px;border-radius:4px}
.copyright{position:absolute;top:3496px;left:0;width:1200px;height:47px;background:var(--footer-deep);color:#bbb;font-size:11.5px;text-align:center;line-height:47px}
</style>
</head>
<body>

<header class="site-header">
  <div class="brand"><span class="brand-dot"></span>Brindle Structures</div>
  <nav class="main-nav">
    <a class="active" href="#">Home</a>
    <a href="#">Portfolio</a>
    <a href="#">Product Specs</a>
    <a href="#">Testimonials</a>
    <a href="#">Our Process</a>
    <a href="#">Contact</a>
  </nav>
</header>

<section class="hero" role="img" aria-label="Two-storey stone house with white garage doors under a blue sky">
  <h1 class="hero-title">Building Dreams,So You Can Build Dreams</h1>
</section>

<section class="services">
  <h2 class="section-title" style="top:44px">Our Services</h2>
  <p class="lead" style="top:96px">Lorem ipsum dolor sit amet, consectetur adipiscing elit. Praesent rutrum sem quam, vel dignissim lacus placerat quis. Nunc et turpis nec massa vulputate efficitur ut Proin accumsan at massa eget dapibus. Ut sollicitudin id est non auctor. Praesent ut tincidunt elit.</p>

  <div class="service" style="left:80px">
    <div class="service-photo" role="img" aria-label="Contractors in hard hats reviewing plans" style="background:linear-gradient(135deg,#2f4a66,#7d8a96)"></div>
    <h3>General Contracting</h3>
    <p>Construction Department Specializing in Commercial Remodeling and Maintenance.</p>
  </div>
  <div class="service" style="left:347px">
    <div class="service-photo" role="img" aria-label="Builders working on a timber frame" style="background:linear-gradient(135deg,#c08660,#6b4a34)"></div>
    <h3>Construction</h3>
    <p>Brindle Structures has spent a century refining our construction and safety practices.</p>
  </div>
  <div class="service" style="left:614px">
    <div class="service-photo" role="img" aria-label="Technician laying floor tiles" style="background:linear-gradient(135deg,#8c8f92,#b9773e)"></div>
    <h3>Commercial Maintenance</h3>
    <p>Brindle Structures has skilled technicians ready to repair and maintain commercial facilities.</p>
  </div>
  <div class="service" style="left:881px">
    <div class="service-photo" role="img" aria-label="Painter rolling paint onto a wall" style="background:linear-gradient(135deg,#8fcfc2,#e8eeea)"></div>
    <h3>Painting</h3>
    <p>Our Painting Division is staffed with professional painters who have lots of experience in the field of projects.</p>
  </div>
</section>

<section class="process">
  <h2 class="section-title" style="top:46px">Our Process</h2>
  <div class="step" style="left:83px">
    <div class="step-icon" style="background:#3dbf4e">
      <svg width="40" height="40" viewBox="0 0 40 40" fill="#fff"><rect x="10" y="6" width="20" height="14" rx="2"/><circle cx="12" cy="26" r="4"/><circle cx="28" cy="26" r="4"/><rect x="6" y="31" width="12" height="6" rx="3"/><rect x="22" y="31" width="12" height="6" rx="3"/></svg>
    </div>
    <h3>Requirement</h3>
    <p>Our home owners show us what work they require to be done.</p>
  </div>
  <div class="step" style="left:438px">
    <div class="step-icon" style="background:#1fb6cb">
      <svg width="40" height="40" viewBox="0 0 40 40" fill="none" stroke="#fff" stroke-width="3"><rect x="7" y="7" width="26" height="18"/><path d="M20 25v8M13 35l7-4 7 4M12 19l6-6 4 4 6-6"/></svg>
    </div>
    <h3>Choice</h3>
    <p>We then offer our clients a choice of guaranteed "Brindle Structures".</p>
  </div>
  <div class="step" style="left:794px">
    <div class="step-icon" style="background:#7b3fbf">
      <svg width="40" height="40" viewBox="0 0 40 40" fill="#fff"><rect x="5" y="12" width="8" height="16"/><rect x="27" y="12" width="8" height="16"/><path d="M13 16h14v9l-7 5-7-5z"/></svg>
    </div>
    <h3>Full Responsibility</h3>
    <p>Once approved by our customers, the people at Brindle Structures then take FULL responsibility to complete the works.</p>
  </div>
</section>

<section class="portfolio">
  <h2 class="section-title" style="top:44px">Portfolio</h2>
  <div class="tile" role="img" aria-label="Modern white house with flat roofs and lawn" style="left:158px;top:116px;width:584px;height:307px;background:linear-gradient(180deg,#7fb3e6 0%,#d8dee3 45%,#8a8f94 62%,#4f8a35 100%)"></div>
  <div class="tile" role="img" aria-label="White house with porch and steps" style="left:768px;top:116px;width:281px;height:307px;background:linear-gradient(180deg,#a7c8e8 0%,#e9ece6 50%,#b9b2a8 75%,#4d7f35 100%)"></div>
  <div class="tile" role="img" aria-label="Suburban house with landscaped garden" style="left:158px;top:439px;width:281px;height:308px;background:linear-gradient(180deg,#9ec3e6 0%,#c8b99c 45%,#c77a3a 70%,#5d9a38 100%)"></div>
  <div class="tile" role="img" aria-label="House at dusk with autumn trees" style="left:463px;top:439px;width:281px;height:308px;background:linear-gradient(180deg,#5a4c8f 0%,#b24a5e 35%,#6b6f9a 65%,#8b8fc0 100%)"></div>
  <div class="tile" role="img" aria-label="Red brick house with green lawn" style="left:768px;top:439px;width:281px;height:308px;background:linear-gradient(180deg,#9fc7e4 0%,#c8c5bf 40%,#9a4a38 62%,#3f7a2e 100%)"></div>
</section>

<section class="products">
  <h2 class="section-title" style="top:44px">Products</h2>
  <p class="lead" style="top:101px">Lorem ipsum dolor sit amet, consectetur adipiscing elit. Praesent rutrum sem quam, vel dignissim lacus placerat quis. Nunc et turpis nec massa vulputate efficitur ut Proin accumsan at massa eget dapibus. Ut sollicitudin id est non auctor. Praesent ut tincidunt elit.</p>
  <div class="carousel">
    <div class="product-feature" role="img" aria-label="Red door product shot">
      <h4>RED DOOR</h4>
      <p>Lorem Ipsum<br>Ipsum Dolor<br>Integrated Red Door</p>
      <span class="btn">VIEW PRODUCT</span>
    </div>
    <div class="abs" role="img" aria-label="Paintbrush dipped in red paint" style="left:406px;top:14px;width:142px;height:213px;background:linear-gradient(180deg,#f2f2f2 0%,#7a4a2a 45%,#d8192a 65%,#e6e6e6 100%)"></div>
    <div class="abs" role="img" aria-label="Open white casement window with red frame" style="left:647px;top:12px;width:302px;height:215px;background:linear-gradient(135deg,#5b3a2e,#c9d8e4 50%,#b52a2a)"></div>
  </div>
  <div class="arrow" style="left:99px;top:276px">
    <svg width="52" height="52" viewBox="0 0 52 52"><path d="M30 16 20 26l10 10" fill="none" stroke="#fff" stroke-width="4"/></svg>
  </div>
  <div class="arrow" style="left:1043px;top:276px">
    <svg width="52" height="52" viewBox="0 0 52 52"><path d="M22 16l10 10-10 10" fill="none" stroke="#fff" stroke-width="4"/></svg>
  </div>
</section>

<section class="testimonials">
  <h2 class="section-title" style="top:44px">Testimonials</h2>
  <div class="quote-card" style="left:90px">
    <span class="mark" style="left:8px;top:-6px">&ldquo;</span>
    <span class="mark" style="right:40px;top:54px">&rdquo;</span>
    <p>Lorem ipsum dolor sit amet, consectetur adipiscing elit. Nulla fermentum dignissim risus eleifend sagittis. Integer turpis mi, hendrerit a leo eu, vestibulum dictum sem. Nullam egestas mauris in dui cursus, nec porta lectus tempus.</p>
    <div class="who">Tom Harlow</div>
    <div class="role">Customer</div>
  </div>
  <div class="avatar" style="left:465px;top:183px" role="img" aria-label="Customer portrait"><span></span></div>

  <div class="quote-card" style="left:616px">
    <span class="mark" style="left:8px;top:-6px">&ldquo;</span>
    <span class="mark" style="right:40px;top:54px">&rdquo;</span>
    <p>Lorem ipsum dolor sit amet, consectetur adipiscing elit. Nulla fermentum dignissim risus eleifend sagittis. Integer turpis mi, hendrerit a leo eu, vestibulum dictum sem. Nullam egestas mauris in dui cursus, nec porta lectus tempus.</p>
    <div class="who">Tom Harlow</div>
    <div class="role">Customer</div>
  </div>
  <div class="avatar" style="left:991px;top:183px" role="img" aria-label="Customer portrait"><span></span></div>
</section>

<footer class="site-footer">
  <div class="foot-col" style="left:80px;width:155px">
    <h5>Navigation</h5>
    <ul class="foot-nav">
      <li>Home</li><li>About</li><li>Services</li><li>Portfolio</li><li>Basalt Family</li><li>Testimonial</li><li>Contact</li>
    </ul>
  </div>
  <div class="foot-col news" style="left:274px;width:265px">
    <h5>News &amp; Updates</h5>
    <div class="news-thumb" role="img" aria-label="Dark modern house at night"></div>
    <p>Lorem ipsum dolor sit amet, consectetur adipiscing elit. Fusce convallis libero quis felis malesuada. Nam ultrices et velit sed maximus.</p>
    <p>Mauris ante nisl, facilisis vel condimentum id, tristique at mauris. Donec ex nisl, lacinia non efficitur id, scelerisque id dolor. Vivamus euismod velit eget velit iaculis placerat.</p>
  </div>
  <div class="foot-col" style="left:579px;width:245px">
    <h5>Our Location</h5>
    <div class="loc-line">
      <svg width="12" height="14" viewBox="0 0 12 14"><path d="M6 0a5 5 0 0 1 5 5c0 4-5 9-5 9S1 9 1 5a5 5 0 0 1 5-5z" fill="#ddd"/><circle cx="6" cy="5" r="2" fill="#2c2c2c"/></svg>
      <span>Street Address Line One Here<br>Town, County and Postcode</span>
    </div>
    <div class="loc-line" style="font-size:15px;align-items:center">
      <svg width="12" height="14" viewBox="0 0 12 14"><path d="M2 1h3l1 3-2 1.5a8 8 0 0 0 4 4L9.5 7l2.5 1v3c0 1-1 2-2 2C5 13 0 8 0 3c0-1 1-2 2-2z" fill="#ddd"/></svg>
      <span>800 555 0142</span>
    </div>
    <div class="loc-line" style="align-items:center">
      <svg width="12" height="10" viewBox="0 0 12 10"><rect width="12" height="10" fill="#ddd"/><path d="M0 0l6 5 6-5" fill="none" stroke="#2c2c2c"/></svg>
      <span>info@brindlestructures.example</span>
    </div>
    <div class="map" role="img" aria-label="Street map of the office location"></div>
  </div>
  <div class="foot-col signup" style="left:864px;width:256px">
    <h5>Newsletter Signup</h5>
    <p>Please enter your email address below to receive our FREE newsletter</p>
    <div class="signup-form"><span>Your Email ID</span><b>Subscribe</b></div>
    <div class="social">
      <i style="background:#2aa6d7"></i><i style="background:#f07a1e"></i><i style="background:#3b5a9a"></i><i style="background:#d3262a"></i>
    </div>
  </div>
</footer>
<div class="copyright">Copyright 2015 @brindlestructures.example. All rights reserved</div>

</body>
</html>
```